Bright Harbor Works Buisness Cards

Provide a business card layout

Paul Wexford
PO Box 742
Millbrook VT 02318
paul@thwexample.com

Industry/Entity Type

Business

Font styles to use
Serif

Colors
f04a50

```html
<!DOCTYPE html>
<html lang="en">
<head>
<meta charset="utf-8">
<title>Bright Harbor Works – Business Card</title>
<link rel="stylesheet" href="https://fonts.googleapis.com/css2?family=Cormorant+SC:wght@600;700&display=swap">
<style>
  :root {
    --brand-red: #9b1017;
    --brand-gold: #e9a532;
    --ink: #1b1b1b;
    --paper: #ffffff;
    --page: #ffffff;
  }
  * { box-sizing: border-box; margin: 0; padding: 0; }
  html, body {
    width: 1200px;
    height: 705px;
    overflow: hidden;
    background: var(--page);
  }
  .business-card {
    position: absolute;
    left: 20px;
    top: 18px;
    width: 1160px;
    height: 664px;
    background: var(--paper);
    border: 1px solid #d6d6d6;
    box-shadow: 2px 3px 8px rgba(0, 0, 0, 0.35);
    overflow: hidden;
    font-family: "Cormorant SC", "Times New Roman", serif;
  }
  .edge-band {
    position: absolute;
    top: 0;
    width: 20px;
    height: 100%;
  }
  .edge-band--left {
    left: 0;
    background: linear-gradient(var(--brand-gold) 0 50%, var(--brand-red) 50% 100%);
  }
  .edge-band--right {
    right: 0;
    background: linear-gradient(var(--brand-red) 0 50%, var(--brand-gold) 50% 100%);
  }
  .holder-name {
    position: absolute;
    left: 56px;
    top: 184px;
    font-size: 50px;
    font-weight: 600;
    color: var(--brand-red);
    letter-spacing: 0.5px;
    line-height: 1;
  }
  .contact-block {
    position: absolute;
    right: 654px;
    top: 364px;
    text-align: right;
    font-size: 36px;
    font-weight: 700;
    font-style: normal;
    color: var(--ink);
    line-height: 42px;
    letter-spacing: 0.5px;
  }
  .divider {
    position: absolute;
    left: 526px;
    top: 197px;
    width: 4px;
    height: 282px;
    background: linear-gradient(var(--brand-gold) 0 48%, var(--brand-red) 48% 100%);
  }
  .company-mark {
    position: absolute;
    left: 540px;
    top: 171px;
    width: 560px;
    text-align: center;
  }
  .company-mark__dot {
    display: block;
    margin: 0 auto 36px;
    width: 170px;
    height: 170px;
  }
  .company-mark__name {
    font-size: 54px;
    font-weight: 700;
    color: var(--ink);
    line-height: 1;
    letter-spacing: 1px;
    white-space: nowrap;
  }
</style>
</head>
<body>
  <div class="business-card">
    <div class="edge-band edge-band--left"></div>
    <div class="edge-band edge-band--right"></div>

    <h1 class="holder-name">Paul Wexford</h1>

    <address class="contact-block">
      <div class="contact-line">PO Box 742</div>
      <div class="contact-line">Millbrook VT 02318</div>
      <div class="contact-line">paul@thwexample.com</div>
    </address>

    <div class="divider"></div>

    <div class="company-mark">
      <svg class="company-mark__dot" viewBox="0 0 170 170" aria-hidden="true">
        <circle cx="85" cy="85" r="85" fill="var(--brand-gold)"/>
      </svg>
      <div class="company-mark__name">Bright Harbor Works</div>
    </div>
  </div>
</body>
</html>
```